Vela Luxe Gel Top Coat & Base Coat Box Design

We are a wholesale nail and beauty supply company located in the USA. We need an attractive box design for our product, Vela Luxe Gel Top Coat and Base Coat, to boost our sales to retail nail salons in the USA.
Dimension of the box is 11'' wide by 8.25'' long.
Color of the box is black with ingrained pattern (see picture).
Need design for top of box only.

Target Market(s)

Retail Nail Salons in the USA

Industry/Entity Type

Beauty Salon

Colors

Designer to choose colors to be used in the design.

Requirements
Must have
• Luxe Vela Gel Top Coat Base Coat
• Matching Font of our product label (see picture)
Nice to have
• LUXE should stand out.
• Line separating design for Top Coat and Base Coat (as they are 2 different products in the same box). Open to all color schemes, but would like to see some in silver.

```html
<!DOCTYPE html>
<html lang="en">
<head>
<meta charset="utf-8">
<title>Vela Luxe Gel Top Coat &amp; Base Coat — Box Top</title>
<link rel="stylesheet" href="https://fonts.googleapis.com/css2?family=Jost:wght@400;500&display=swap">
<style>
  :root {
    --stage: #a4a4a4;
    --box-black: #060404;
    --gold-foil: #a0823a;
    --label-white: #ffffff;
  }
  * { box-sizing: border-box; margin: 0; padding: 0; }
  html, body {
    width: 1135px;
    height: 1200px;
    overflow: hidden;
    background: var(--stage);
  }
  .canvas {
    position: relative;
    width: 1135px;
    height: 1200px;
  }
  .box-top {
    position: absolute;
    left: 117px;
    top: 323px;
    width: 660px;
    height: 406px;
    background: var(--box-black);
    transform: scale(1.3636);
    transform-origin: 0 0;
    font-family: "Jost", "Futura", sans-serif;
  }
  .gold-frame {
    position: absolute;
    left: 23px;
    top: 22px;
    width: 614px;
    height: 362px;
    border: 4px solid var(--gold-foil);
  }
  .tier-title {
    position: absolute;
    left: 0;
    right: 0;
    top: 12px;
    text-align: center;
    line-height: 38px;
  }
  .tier-title span {
    display: inline-block;
    padding: 0 16px;
    background: var(--box-black);
    color: var(--gold-foil);
    font-weight: 500;
    font-size: 34px;
    letter-spacing: 3px;
  }
  .foil-bar {
    position: absolute;
    top: 101px;
    width: 202px;
    height: 74px;
    background: var(--gold-foil);
  }
  .foil-bar--left { left: 48px; }
  .foil-bar--right { left: 410px; }
  .brand-name {
    position: absolute;
    left: 250px;
    width: 160px;
    top: 101px;
    height: 74px;
    line-height: 74px;
    text-align: center;
    color: var(--gold-foil);
    font-weight: 500;
    font-size: 40px;
    letter-spacing: 2px;
  }
  .product-lines {
    position: absolute;
    left: 83px;
    top: 241px;
    width: 494px;
    height: 66px;
    border: 2px solid var(--gold-foil);
    display: flex;
    align-items: center;
    justify-content: center;
    gap: 12px;
    color: var(--label-white);
    font-size: 28px;
    font-weight: 400;
    white-space: nowrap;
  }
  .product-divider {
    width: 2px;
    height: 28px;
    background: var(--gold-foil);
  }
</style>
</head>
<body>
  <main class="canvas">
    <section class="box-top" aria-label="Vela Luxe Gel Top Coat and Base Coat box top">
      <div class="gold-frame"></div>
      <h1 class="tier-title"><span>LUXE</span></h1>
      <div class="foil-bar foil-bar--left"></div>
      <p class="brand-name">VELA</p>
      <div class="foil-bar foil-bar--right"></div>
      <p class="product-lines">
        <span>GEL TOP COAT</span>
        <span class="product-divider"></span>
        <span>GEL BASE COAT</span>
      </p>
    </section>
  </main>
</body>
</html>
```